Business card design needed

We need a business card design for our new company Velbrino Event Creations, based in Leeton NSW. We will however be serving the whole Riverina area. We plan any events like, Parties, Weddings ext. We would like to see designs that is vibrant but elegant. Mainly we would like to have our Name displayed on the front and all the other info at the back. We need a design that will catch the eye anywhere.Design FRONT AND BACK

Industry/Entity Type

Events

Contact Information for Business Card

Velbrino Event Creations
Tirsa Hallveck

0461539207
velbrino@quorvamail.com

Believe the Impossible

Requirements
Must have
• Elegant Coulors and Fonts

```html
<!DOCTYPE html>
<html lang="en">
<head>
<meta charset="utf-8">
<title>Velbrino Event Creations – Business Card</title>
<link rel="stylesheet" href="https://fonts.googleapis.com/css2?family=Exo+2:wght@400;500;600&display=swap">
<style>
  :root {
    --bg: #16191b;
    --card-dark: #1d1e20;
    --card-dark-edge: #26282b;
    --paper-light: #ffffff;
    --paper-shade: #d9dadb;
    --lime: #7ed321;
    --lime-soft: #6cbf1a;
    --ink: #3a3c3f;
    --icon-box: #2c2f33;
    --icon-line: #4a4e53;
  }
  * { margin: 0; padding: 0; box-sizing: border-box; }
  html, body {
    width: 1200px; height: 900px; overflow: hidden;
    background: var(--bg);
    font-family: "Exo 2", sans-serif;
  }
  .canvas {
    position: relative; width: 1200px; height: 900px;
    display: flex; flex-direction: column; align-items: center; justify-content: center; gap: 50px;
  }
  .card {
    position: relative; width: 660px; height: 377px;
    border-radius: 4px; overflow: hidden;
    box-shadow: 0 14px 40px rgba(0,0,0,.55);
  }

  /* Front side */
  .card-front { display: flex; flex-direction: column; align-items: center; justify-content: center; gap: 22px; }
  .pattern-fill {
    position: absolute; inset: 0;
    background: radial-gradient(ellipse at center, var(--card-dark-edge), var(--card-dark) 75%);
  }
  .wordmark {
    position: relative; color: var(--lime); font-weight: 500;
    text-align: center; line-height: 1.05;
  }
  .wordmark .name { display: block; font-size: 64px; letter-spacing: 1px; }
  .wordmark .line { display: block; font-size: 28px; letter-spacing: 3px; text-transform: uppercase; }
  .tagline {
    position: relative; color: var(--lime); font-weight: 500;
    font-size: 24px; letter-spacing: 1px;
  }

  /* Back side */
  .card-back { display: flex; }
  .logo-panel {
    width: 55%; display: flex; align-items: center; justify-content: center;
    background: linear-gradient(135deg, var(--paper-light) 20%, var(--paper-shade));
  }
  .logo-panel .wordmark .name { font-size: 52px; }
  .logo-panel .wordmark .line { font-size: 23px; }
  .contact-panel {
    position: relative; width: 45%; padding: 40px 20px 0 22px;
  }
  .holder {
    position: relative; color: var(--lime); font-weight: 600;
    font-size: 20px; letter-spacing: 3px; text-transform: uppercase; margin-bottom: 16px;
  }
  .contact-list { position: relative; list-style: none; }
  .contact-list li {
    display: flex; align-items: center; gap: 10px;
    color: var(--lime-soft); font-size: 17px; letter-spacing: .5px;
    margin-bottom: 14px; white-space: nowrap;
  }
  .icon {
    flex: none; width: 24px; height: 24px; border-radius: 4px;
    background: var(--icon-box); border: 1px solid var(--icon-line);
    display: flex; align-items: center; justify-content: center;
  }
  .icon svg { width: 14px; height: 14px; }
</style>
</head>
<body>
<main class="canvas">

  <section class="card card-front" aria-label="Card front">
    <div class="pattern-fill" role="img" aria-label="Dark damask pattern background"></div>
    <div class="wordmark">
      <span class="name">Velbrino</span>
      <span class="line">Event Creations</span>
    </div>
    <p class="tagline">Believe the Impossible</p>
  </section>

  <section class="card card-back" aria-label="Card back">
    <div class="logo-panel">
      <div class="wordmark">
        <span class="name">Velbrino</span>
        <span class="line">Event Creations</span>
      </div>
    </div>
    <div class="contact-panel">
      <div class="pattern-fill" role="img" aria-label="Dark damask pattern background"></div>
      <p class="holder">Tirsa Hallveck</p>
      <ul class="contact-list">
        <li>
          <span class="icon">
            <svg viewBox="0 0 16 16"><path d="M4 1.5l2.5 3-1.5 1.5c.8 2 2.4 3.6 4.5 4.5L11 9l3 2.5-1.5 2.5C7 14 2 9 1.5 3.5z" fill="var(--lime)"/></svg>
          </span>0461539207
        </li>
        <li>
          <span class="icon">
            <svg viewBox="0 0 16 16"><rect x="1.5" y="3.5" width="13" height="9" fill="none" stroke="var(--lime)" stroke-width="1.5"/><path d="M1.5 3.5L8 9l6.5-5.5" fill="none" stroke="var(--lime)" stroke-width="1.5"/></svg>
          </span>velbrino@quorvamail.com
        </li>
        <li><span class="icon"></span>Velbrino Creations</li>
        <li><span class="icon"></span>@velbrino</li>
        <li><span class="icon"></span>Velbrino Event Creations</li>
      </ul>
    </div>
  </section>

</main>
</body>
</html>
```